Ayurvedic Beauty Company in Need of Business Cards

My company is a high-end ayurvedic beauty brand. I need a business card that represents that. The designer should utilize logo and color palette. I want these cards to be printed with the foil accents so keep that in mind.

I have attached the ai of my logo and business card info. As well as, some of the product we are launching soon, they do not have to be on the card.

Be creative and have fun.

Thanks in advance,

Marla

```html
<!DOCTYPE html>
<html lang="en">
<head>
<meta charset="utf-8">
<title>Amber Vale — Business Cards</title>
<link href="https://fonts.googleapis.com/css2?family=Cinzel:wght@400&family=Montserrat:wght@600&family=Quicksand:wght@400&display=swap" rel="stylesheet">
<style>
  :root {
    --stage-light: #e6e7e9;
    --stage-dark: #000000;
    --plum-top: #5a1545;
    --plum-bottom: #992f71;
    --gold: #b08752;
    --gold-light: #c9a877;
    --ivory: #ffffff;
  }
  * { margin: 0; padding: 0; box-sizing: border-box; }
  html, body { width: 1200px; height: 1200px; overflow: hidden; }
  body {
    position: relative;
    background: linear-gradient(to bottom right, var(--stage-light) 50%, var(--stage-dark) 50%);
  }
  .card {
    position: absolute;
    top: 180px;
    width: 480px;
    height: 839px;
    background: linear-gradient(to bottom, var(--plum-top), var(--plum-bottom));
    overflow: hidden;
  }
  .card--front { left: 95px; }
  .card--back { left: 625px; }
  .card__band {
    position: absolute; left: 0; right: 0; bottom: 0; height: 18px;
    background: var(--gold);
  }
  .brand {
    position: absolute; left: 0; right: 0;
    text-align: center;
  }
  .brand__mark {
    display: block;
    width: 150px; height: 150px;
    margin: 0 auto 36px;
    border-radius: 50%;
    background: var(--gold);
  }
  .brand__name {
    font-family: "Montserrat", sans-serif;
    font-weight: 600;
    font-size: 44px;
    letter-spacing: 1px;
    color: var(--gold-light);
    line-height: 1;
  }
  .card--front .brand { top: 90px; }
  .card--back .brand { top: 298px; }
  .person {
    position: absolute; top: 420px; left: 0; right: 0;
    text-align: center;
  }
  .person__name {
    font-family: "Cinzel", serif;
    font-size: 46px;
    color: var(--ivory);
    line-height: 1;
    letter-spacing: 0.5px;
  }
  .person__role {
    display: flex; align-items: center; justify-content: center;
    gap: 12px;
    margin-top: 10px;
    font-family: "Quicksand", sans-serif;
    font-size: 28px;
    color: var(--ivory);
    line-height: 1;
  }
  .person__rule { width: 134px; height: 2px; background: var(--gold); }
  .contact-icons {
    position: absolute; top: 624px; left: 0; right: 0;
    display: flex; justify-content: center; align-items: center; gap: 8px;
  }
  .contact-icons__sep { width: 2px; height: 24px; background: var(--gold); }
  .contact-icons svg { width: 26px; height: 26px; display: block; }
  .contact-list {
    position: absolute; top: 668px; left: 0; right: 0;
    list-style: none;
    text-align: center;
    font-family: "Quicksand", sans-serif;
    font-size: 25px;
    line-height: 34px;
    color: var(--ivory);
  }
</style>
</head>
<body>
  <section class="card card--front">
    <div class="brand">
      <span class="brand__mark"></span>
      <div class="brand__name">AMBER VALE</div>
    </div>
    <div class="person">
      <div class="person__name">MARLA DOVANE</div>
      <div class="person__role"><span class="person__rule"></span>CEO<span class="person__rule"></span></div>
    </div>
    <div class="contact-icons" aria-hidden="true">
      <svg viewBox="0 0 26 26"><circle cx="13" cy="13" r="13" fill="#fff"/><rect x="9" y="6" width="8" height="14" rx="1.5" fill="none" stroke="#6b1d52" stroke-width="2"/></svg>
      <span class="contact-icons__sep"></span>
      <svg viewBox="0 0 26 26"><circle cx="13" cy="13" r="13" fill="#fff"/><path d="M8 7c1-1 2-1 3 0l1 2c.4 1 0 1.6-.8 2.2.8 1.6 2 2.8 3.6 3.6.6-.8 1.2-1.2 2.2-.8l2 1c1 1 1 2 0 3-2 2-5 1-8-2s-5-6-3-9z" fill="#6b1d52"/></svg>
      <span class="contact-icons__sep"></span>
      <svg viewBox="0 0 26 26"><circle cx="13" cy="13" r="13" fill="#fff"/><rect x="6" y="8" width="14" height="10" rx="1.5" fill="#6b1d52"/><path d="M6.5 9l6.5 5 6.5-5" fill="none" stroke="#fff" stroke-width="1.5"/></svg>
      <span class="contact-icons__sep"></span>
      <svg viewBox="0 0 26 26"><circle cx="13" cy="13" r="13" fill="#fff"/><path d="M8 18l10-10" stroke="#6b1d52" stroke-width="4" stroke-linecap="round"/><path d="M11 15l4-4" stroke="#fff" stroke-width="1.5"/></svg>
    </div>
    <ul class="contact-list">
      <li>1(347) 555-0142</li>
      <li>1(888) 555-0186</li>
      <li>marla@loveambervale.com</li>
      <li>www.loveambervale.com</li>
    </ul>
    <div class="card__band"></div>
  </section>

  <section class="card card--back">
    <div class="brand">
      <span class="brand__mark"></span>
      <div class="brand__name">AMBER VALE</div>
    </div>
    <div class="card__band"></div>
  </section>
</body>
</html>
```